KVR Associates needs a web site

We need a web site for www.kvrassociates-example.com. KVR is a mergers and acquisition consulting company that focuses our buyer and seller services on logistics companies. We help put companies together, and help with legal and financial due diligence. We want the web site to express our service and show the logistics components. We want personalized images versus pictures of trucks and airplanes.

Our new logo uses Burgandy and grey colors. Image attached. We are not in to bold, big letters...classy, artistic, low key preferred. Confidentiality, experience, professional are what we want to express on the site.

All we expect for the first part of this project is a home page, and one subpage.  We are budgeting other funds for the technical aspects of the web site

Reason: All that I'm seeing so far is trucks, forklifts and planes. We are a legal mergers and acquisitions firm that focus on logistics. I like some of the images to say logistics, but really want it say legal, financial, and putting companies together. Will pay extra for the sub page if someone can impress us with a home page.

Reason: Swamped with another project at the moment...will work on this over the weekend and provide designer feedback and select final design by Tuesday

```html
<!DOCTYPE html>
<html lang="en">
<head>
<meta charset="utf-8">
<title>KVR Associates</title>
<link href="https://fonts.googleapis.com/css2?family=Source+Sans+3:wght@400;600&display=swap" rel="stylesheet">
<style>
:root{
  --page:#f6f7f8;
  --ink:#333a40;
  --text:#4a4f55;
  --grey:#5d6369;
  --red:#e3262f;
  --burgundy:#9c1b2e;
  --panel:#dde0e1;
  --footer:#1f2224;
  --bar:rgba(40,42,44,.88);
}
*{margin:0;padding:0;box-sizing:border-box}
html,body{width:1010px;height:1200px;overflow:hidden}
body{background:var(--page);font-family:"Source Sans 3",sans-serif;color:var(--text);position:relative}
.abs{position:absolute}

.brand{left:56px;top:46px;display:flex;align-items:center;gap:10px}
.brand-mark{width:26px;height:26px;background:var(--burgundy)}
.brand-name{font-size:30px;font-weight:400;letter-spacing:2px;color:var(--grey)}

.register{left:579px;top:42px;width:72px;height:24px;background:var(--burgundy);color:#fff;font-size:13px;line-height:24px;text-align:center}
.search{left:662px;top:44px;width:200px;height:22px;border:1px solid #cfd3d6;background:#f1f2f3;font-size:12px;line-height:20px;padding-left:6px;color:#333}
.search svg{position:absolute;right:4px;top:3px}
.social-top{left:872px;top:41px;display:flex;gap:6px}
.social-top span{width:25px;height:25px;background:#8d949a;display:block}

.nav{left:630px;top:90px;display:flex;gap:30px;font-size:13.5px;color:#7a8086}
.nav a{color:inherit;text-decoration:none;padding-bottom:2px}
.nav .active{color:var(--red);border-bottom:2px solid var(--red)}

.hero{left:56px;top:118px;width:897px;height:411px;background:linear-gradient(180deg,#9ec6e4 0%,#c9dceb 42%,#b9bcbd 58%,#9a9c9b 100%)}
.hero-title{left:48px;top:86px;font-size:46px;color:var(--red);font-weight:400;letter-spacing:.3px}
.hero-sub{left:53px;top:140px;font-size:15px;color:#fff;line-height:16.5px}
.hero-btn{left:307px;top:180px;width:78px;height:26px;background:var(--red);color:#fff;font-size:12.5px;line-height:26px;text-align:center}
.dots{left:424px;top:341px;display:flex;gap:5px}
.dots span{width:12px;height:12px;border-radius:50%;background:#e9ecee;border:1px solid #b8bcbf}
.updates{left:0;top:374px;width:897px;height:37px;background:var(--bar);color:#fff;font-size:13.5px;line-height:37px;padding-left:65px}
.updates b{font-weight:600}

h2{font-weight:400;color:var(--ink);font-size:25px}
h2 em{font-style:normal;color:var(--red)}
.welcome{left:67px;top:550px}
.why{left:72px;top:724px}
.copy{font-size:12px;line-height:15.6px;color:var(--text);width:780px}
.p1{left:74px;top:596px}
.p2{left:74px;top:658px}
.p3{left:78px;top:763px}

.services{left:72px;top:822px;width:862px;height:228px;background:var(--panel);border:1px solid #cfd3d5}
.services h3{position:absolute;left:37px;top:18px;font-weight:400;font-size:22px;color:var(--ink)}
.services h3 em{font-style:normal;color:var(--red)}
.card{position:absolute;top:49px;width:205px}
.card-title{height:26px;background:#3d4a57;color:#fff;font-size:15.5px;line-height:26px;text-align:center}
.card-img{height:102px}
.sea{background:linear-gradient(180deg,#9cc8e8 0%,#bcd7ea 45%,#2f6f93 62%,#1c4e6d 100%)}
.air{background:linear-gradient(180deg,#d9dde0 0%,#b7bcc0 55%,#6b6d68 100%)}
.card-btn{position:absolute;right:0;top:142px;width:64px;height:21px;background:var(--red);color:#fff;font-size:10.5px;line-height:21px;text-align:center}

.footer{left:0;top:1058px;width:1010px;height:142px;background:var(--footer);border-top:4px solid var(--red)}
.footer-brand{left:24px;top:40px;display:flex;align-items:center;gap:9px}
.footer-brand .brand-mark{width:20px;height:20px;background:#fff}
.footer-brand .brand-name{font-size:22px;color:#fff}
.copyright{left:29px;top:98px;font-size:9.5px;color:#d7d9db}
.footer-nav{left:416px;top:48px;display:flex;gap:22px;font-size:11px;color:#fff}
.follow{left:881px;top:52px;font-size:12.5px;color:#fff}
.social-foot{left:882px;top:74px;display:flex;gap:8px}
.social-foot span{width:31px;height:31px;background:#7f868c;display:block}
</style>
</head>
<body>

<header>
  <div class="abs brand"><span class="brand-mark"></span><span class="brand-name">KVR ASSOCIATES</span></div>
  <div class="abs register">REGISTER</div>
  <div class="abs search">Search
    <svg width="14" height="14" viewBox="0 0 14 14"><circle cx="5.5" cy="5.5" r="4" fill="none" stroke="#6a6f74" stroke-width="1.8"/><line x1="8.5" y1="8.5" x2="13" y2="13" stroke="#6a6f74" stroke-width="2"/></svg>
  </div>
  <div class="abs social-top" aria-label="Social profiles"><span></span><span></span><span></span></div>
  <nav class="abs nav"><a class="active">HOME</a><a>ABOUT US</a><a>SERVICES</a><a>CONTACT US</a></nav>
</header>

<section class="abs hero" role="img" aria-label="Cargo aircraft being loaded on an airport apron">
  <div class="abs hero-title">KVR PROFESSIONALS</div>
  <div class="abs hero-sub">KVR can help you formulate and execute your growth strategy<br>We take a strategic and consultative approach</div>
  <div class="abs hero-btn">READ MORE</div>
  <div class="abs dots"><span></span><span></span><span></span><span></span><span></span></div>
  <div class="abs updates"><b>LATEST UPDATES:</b> KVR can help you formulate and execute your growth strateg we take a strategic and consultative approach</div>
</section>

<main>
  <h2 class="abs welcome">Welcome to <em>KVR Associates</em></h2>
  <p class="abs copy p1">KVR assists business owners within the logistics industry to implement growth and exit strategies. We offer business planning and merger<br>&nbsp;and acquisition(M&amp;A) advisory services. KVR services are offered by industry executives with extensive M&amp;A experience.&nbsp; Your company will<br>benefit from a unique and outside perspective from consultants that understand your business.</p>
  <p class="abs copy p2" style="width:800px">KVR can help you formulate and execute your growth strategy. We take a strategic and consultative approach with our advisory services that<br>&nbsp;will help you grow your business effectively.&nbsp; Since our experience and focus is only in the logistics space, you can be confident that our process<br>&nbsp;will be efficient and streamlined as we help achieve your goals.</p>

  <h2 class="abs why">Why <em>Us</em></h2>
  <p class="abs copy p3">KVR assists business owners within the logistics industry to implement growth and exit strategies. We offer business planning and merger<br>&nbsp;and acquisition(M&amp;A) advisory services. KVR services are offered by industry executives with extensive M&amp;A experience.&nbsp; Your company will<br>benefit from a unique and outside perspective from consultants that understand your business.</p>

  <section class="abs services">
    <h3>OUR <em>SEVICES</em></h3>
    <div class="card" style="left:36px">
      <div class="card-title">Growth &amp; Exit Strategies</div>
      <div class="card-img sea" role="img" aria-label="Container ship at sea"></div>
      <div class="card-btn">READ MORE</div>
    </div>
    <div class="card" style="left:323px">
      <div class="card-title">Growth &amp; Exit Strategies</div>
      <div class="card-img air" role="img" aria-label="Airliner being serviced on the apron"></div>
      <div class="card-btn">READ MORE</div>
    </div>
    <div class="card" style="left:617px">
      <div class="card-title">Growth &amp; Exit Strategies</div>
      <div class="card-img sea" role="img" aria-label="Container ship at sea"></div>
      <div class="card-btn">READ MORE</div>
    </div>
  </section>
</main>

<footer class="abs footer">
  <div class="abs footer-brand"><span class="brand-mark"></span><span class="brand-name">KVR ASSOCIATES</span></div>
  <div class="abs copyright">COPYRIGHT &copy; 2014 KVR ASSOCIATES. ALL RIGHTS RESERVED</div>
  <nav class="abs footer-nav"><span>HOME</span><span>ABOUT US</span><span>SERVICES</span><span>CONTACT US</span></nav>
  <div class="abs follow">FOLLOW US</div>
  <div class="abs social-foot" aria-label="Social profiles"><span></span><span></span><span></span></div>
</footer>

</body>
</html>
```